Re-brand our business and design!

We need a simple informational website (editable for in the future use)
We need our logo(we have included logo), name, who we are, and what we do displayed.

This is our current site (which is not acceptable, and only a template site): all our information is on this site, please use it forreferanceofinformation.
Www.brightlanefixers.com

Target Market(s)

Real estate brokers, and realtors,homeowners, and anyone looking for home repairs.

Industry/Entity Type

Business

Number of Pages Required

4 page

Font styles to use
Sans Serif

Requirements
Must have
• Our name, contact info, services, and our logo (which we will Email upon request)
• MUST have originality to the site.
• custom "contact us form" or request an estimate form.
Nice to have
• page for real customer testimonies.
• page for our previous work where we can upload pics of completed jobs.
Should not have
• any infringements on any copyrights or plagiarism at all.

```html
<!DOCTYPE html>
<html lang="en">
<head>
<meta charset="utf-8">
<title>Brightlane Home Repairs And Maintenance</title>
<link href="https://fonts.googleapis.com/css2?family=Raleway:wght@500;600;700;800&family=Open+Sans:wght@400;600;700&display=swap" rel="stylesheet">
<style>
:root{
  --red:#e30613;
  --dark:#1c1c1c;
  --charcoal:#3d3d3d;
  --grey-bg:#f2f2f2;
  --text:#444;
  --muted:#777;
  --white:#fff;
}
*{margin:0;padding:0;box-sizing:border-box}
html,body{width:1200px;height:3742px;overflow:hidden}
body{font-family:"Open Sans",Arial,sans-serif;color:var(--text);background:var(--white);position:relative}
.abs{position:absolute}
.heading{font-family:"Raleway",Arial,sans-serif;font-weight:700;color:#222;text-align:center;letter-spacing:1px}

/* top bar */
.topbar{top:0;left:0;width:1200px;height:30px;background:var(--red);color:#fff;font-size:13px}
.topbar .addr{left:45px;top:6px;display:flex;align-items:center;gap:6px}
.topbar .social{right:30px;top:3px;display:flex;gap:6px}
.topbar .social span{width:22px;height:22px;background:#fff;transform:rotate(45deg) scale(.75);display:block}

/* header */
.header{top:30px;left:0;width:1200px;height:125px;background:#fff}
.brand{left:45px;top:38px;display:flex;align-items:center;gap:10px}
.brand-mark{width:26px;height:26px;background:var(--red)}
.brand-name{font-family:"Raleway",sans-serif;font-weight:800;font-size:22px;color:#222;line-height:1.1}
.contact{top:42px;display:flex;align-items:center;gap:14px}
.contact small{display:block;font-size:10px;color:var(--muted);letter-spacing:1px}
.contact b{font-size:16px;color:#333;font-weight:600}

/* nav */
.nav{top:155px;left:0;width:1200px;height:45px;background:#111}
.nav ul{list-style:none;display:flex;position:absolute;left:60px;top:0;height:45px}
.nav li{font-family:"Raleway",sans-serif;font-weight:700;font-size:14px;color:#fff;padding:0 25px;line-height:45px}
.nav li.active{background:var(--red);clip-path:polygon(0 0,100% 0,88% 100%,0 100%)}
.nav .quote{right:65px;top:0;height:45px;width:185px;background:var(--red);color:#fff;font-family:"Raleway",sans-serif;font-weight:700;font-size:14px;line-height:45px;padding-left:18px;clip-path:polygon(0 0,100% 0,90% 100%,0 100%)}

/* hero */
.hero{top:200px;left:0;width:1200px;height:503px;background:linear-gradient(90deg,#e9e4dc 0%,#d8cfc2 45%,#c9a54a 70%,#8c8c8c 100%)}
.hero-copy{left:45px;top:118px;width:560px}
.hero-copy h1{font-family:"Raleway",sans-serif;font-weight:800;font-size:46px;line-height:1.1;color:#111;padding:14px 15px 0}
.hero-copy h1 span{color:var(--red)}
.hero-copy p{font-size:15px;color:#fff;margin-top:10px;line-height:1.45;padding:12px 15px;background:rgba(60,52,44,.62)}

/* services */
.services{top:703px;left:0;width:1200px;height:654px}
.services h2{top:42px;width:1200px;font-size:34px}
.services .sub{top:95px;width:1200px;text-align:center;font-size:15px;color:#333}
.service{width:290px;text-align:center}
.ring{width:240px;height:240px;border-radius:50%;margin:0 auto;display:flex;flex-direction:column;align-items:center;justify-content:center;font-size:15px;color:#333;gap:10px}
.ring.red{background:var(--red);box-shadow:inset 0 0 0 20px var(--red),inset 0 0 0 28px #fff;color:#fff}
.ring.dark{border:16px solid var(--charcoal);background:#fff}
.service p{font-size:14px;line-height:1.5;color:#444;margin-top:38px}
.more{width:34px;height:34px;border-radius:50%;background:#222;margin:20px auto 0;display:flex;align-items:center;justify-content:center}

/* band */
.band{top:1357px;left:0;width:1200px;height:158px;background:var(--charcoal)}
.band-photo{left:0;top:0;width:425px;height:158px;background:linear-gradient(90deg,#e6e9ec,#7a8796);clip-path:polygon(0 0,82% 0,100% 50%,82% 100%,0 100%)}
.band p{left:445px;top:28px;width:720px;font-size:21px;line-height:1.5;color:#fff}

/* what we do */
.what{top:1515px;left:0;width:1200px;height:593px}
.what h2{top:58px;width:1200px;font-size:34px}
.rule-sub{width:1200px;text-align:center;font-size:13px;color:#333}
.rule-sub::before,.rule-sub::after{content:"";display:inline-block;width:110px;height:1px;background:#999;vertical-align:middle;margin:0 12px}
.what .card{left:45px;top:165px;width:793px;height:353px;border:1px solid #ddd;background:#fff}
.card-photo{left:0;top:0;width:325px;height:353px;background:linear-gradient(135deg,#dcdfe3,#9aa3ad 60%,#c8a27e)}
.card-text{left:342px;top:35px;width:430px}
.card-text h3{font-family:"Raleway",sans-serif;font-weight:700;font-size:20px;color:#222;margin-bottom:16px}
.card-text p{font-size:13.5px;line-height:1.55;color:#555;margin-bottom:16px}
.estimate{left:873px;top:165px;width:283px;height:353px;background:var(--red);padding:22px 18px}
.estimate h3{font-family:"Raleway",sans-serif;font-weight:600;font-size:18px;color:#fff;margin-bottom:20px;white-space:nowrap}
.field{background:#fff;height:30px;margin-bottom:10px;font-size:11px;color:#aaa;padding:7px 8px}
.field.msg{height:90px}
.submit{float:right;background:#111;color:#fff;font-size:12px;font-weight:700;padding:8px 14px;margin-top:8px}

/* completed works */
.works{top:2108px;left:0;width:1200px;height:786px;background:var(--grey-bg)}
.works h2{top:38px;width:1200px;font-size:34px}
.filters{top:145px;left:0;width:1200px;display:flex;justify-content:center;gap:20px}
.filters span{font-size:14px;color:#333;border:1px solid #999;padding:8px 22px;background:#fff}
.filters span.on{background:var(--red);border-color:var(--red);color:#fff;padding:8px 40px}
.grid{top:232px;left:0;width:1200px;display:grid;grid-template-columns:repeat(5,240px);grid-auto-rows:225px}
.grid div:nth-child(odd){background:linear-gradient(135deg,#8aa3c0,#3a5a85)}
.grid div:nth-child(even){background:linear-gradient(135deg,#cfd3d7,#767f88)}
.grid div:nth-child(3n){background:linear-gradient(135deg,#d8c8b0,#7d6e5a)}
.view-all{top:718px;left:550px;width:103px;height:38px;background:var(--red);color:#fff;font-size:15px;text-align:center;line-height:38px}

/* testimonials */
.testi{top:2894px;left:0;width:1200px;height:556px}
.testi h2{top:55px;width:1200px;font-size:34px}
.quote-box{top:180px;height:182px;font-size:14px;line-height:1.6;color:#fff;padding:40px 25px}
.quote-box.red{left:75px;width:526px;background:var(--red)}
.quote-box.dark{left:601px;width:527px;background:#222;text-align:center;font-size:13.5px;padding-top:65px}
.tail{width:0;height:0;border-left:14px solid transparent;border-right:14px solid transparent;border-top:18px solid}
.person{display:flex;align-items:center;gap:20px}
.avatar{width:100px;height:100px;border-radius:50%;background:radial-gradient(circle,#e9d2c0,#b79a84);border:4px solid #eee}
.person b{font-family:"Raleway",sans-serif;font-size:16px;color:#222;display:block}
.person small{font-size:12px;color:#555}

/* footer */
.footer{top:3450px;left:0;width:1200px;height:292px;background:var(--dark);color:#fff;text-align:center}
.footer .brand-name{color:#fff;font-size:24px}
.footer .links{top:135px;width:1200px;font-size:15px}
.footer .copy{top:168px;width:1200px;font-size:14px}
.footer .social{top:220px;left:512px;display:flex;gap:14px}
.footer .social span{width:36px;height:36px;background:#fff;transform:rotate(45deg) scale(.78);display:block}
</style>
</head>
<body>

<div class="abs topbar">
  <div class="abs addr">
    <svg width="12" height="16" viewBox="0 0 12 16"><path d="M6 0a6 6 0 0 0-6 6c0 4.5 6 10 6 10s6-5.5 6-10a6 6 0 0 0-6-6zm0 8.5A2.5 2.5 0 1 1 6 3.5a2.5 2.5 0 0 1 0 5z" fill="#fff"/></svg>
    18, Harbor Lane-42, Northfield
  </div>
  <div class="abs social"><span></span><span></span><span></span><span></span></div>
</div>

<header class="abs header">
  <div class="abs brand">
    <div class="brand-mark"></div>
    <div class="brand-name">Brightlane Home Repairs<br><span style="font-size:13px">And Maintenance</span></div>
  </div>
  <div class="abs contact" style="left:712px">
    <svg width="24" height="36" viewBox="0 0 24 36"><rect x="2" y="1" width="20" height="34" rx="3" fill="none" stroke="#777" stroke-width="2"/><line x1="9" y1="30" x2="15" y2="30" stroke="#777" stroke-width="2"/></svg>
    <div><small>CALL US TODAY</small><b>416-555-0193</b></div>
  </div>
  <div class="abs contact" style="left:908px">
    <svg width="34" height="28" viewBox="0 0 34 28"><rect x="1" y="1" width="32" height="26" fill="none" stroke="#777" stroke-width="2"/><path d="M1 1l16 14L33 1" fill="none" stroke="#777" stroke-width="2"/></svg>
    <div><small>EMAIL US NOW</small><b>help@brightlanefixers.com</b></div>
  </div>
</header>

<nav class="abs nav">
  <ul>
    <li class="active">HOME</li><li>ABOUT</li><li>SERVICES</li><li>PROJECTS</li><li>BLOG</li><li>CONTACT</li>
  </ul>
  <div class="abs quote">REQUEST A QUOTE</div>
</nav>

<section class="abs hero" role="img" aria-label="Handyman with tool belt, wrench and hard hat in a bright room under renovation">
  <div class="abs hero-copy">
    <h1>QUALITY SERVICES<br><span>MATERIALS</span></h1>
    <p>Lorem ipsum dolor sit amet, coetuer adipiscing elit. Praesent vestibulum molestie lacus. Aenean dis parturient montes, nascetur ridiculus mus.</p>
  </div>
</section>

<section class="abs services">
  <h2 class="abs heading">HOME REPAIR SERVICES</h2>
  <div class="abs sub">Serving the Maple Ridge, and surrounding areas</div>

  <div class="abs service" style="left:122px;top:155px">
    <div class="ring red">
      <svg width="44" height="44" viewBox="0 0 44 44" fill="none" stroke="#fff" stroke-width="2.5"><path d="M10 20a12 12 0 0 1 24 0z"/><line x1="6" y1="20" x2="38" y2="20"/><path d="M8 42c0-8 6-13 14-13s14 5 14 13"/><path d="M15 22a7 7 0 0 0 14 0"/></svg>
      CARPENTRY
    </div>
    <p>Lorem ipsum dolor sit amet, consec-<br>teter adipiscing elit. Aenean commo-<br>do ligula eget dolor. Aenean massa.<br>Cum sociis natoque.</p>
    <div class="more"><svg width="12" height="12"><path d="M6 1v10M1 6h10" stroke="#fff" stroke-width="2"/></svg></div>
  </div>

  <div class="abs service" style="left:484px;top:155px">
    <div class="ring dark">
      <svg width="44" height="44" viewBox="0 0 44 44" fill="#333"><rect x="6" y="6" width="20" height="10"/><rect x="18" y="6" width="10" height="26"/><rect x="4" y="4" width="4" height="14"/><path d="M23 36c-2 3-2 5 0 6 2-1 2-3 0-6z"/></svg>
      PLUMBING
    </div>
    <p>Lorem ipsum dolor sit amet, consec-<br>teter adipiscing elit. Aenean commo-<br>do ligula eget dolor. Aenean massa.<br>Cum sociis natoque.</p>
    <div class="more"><svg width="12" height="12"><path d="M6 1v10M1 6h10" stroke="#fff" stroke-width="2"/></svg></div>
  </div>

  <div class="abs service" style="left:826px;top:155px">
    <div class="ring dark">
      <svg width="44" height="44" viewBox="0 0 44 44" fill="none" stroke="#333" stroke-width="2.5"><circle cx="12" cy="9" r="6"/><line x1="12" y1="15" x2="12" y2="40"/><line x1="32" y1="4" x2="32" y2="22"/><rect x="28" y="22" width="8" height="18"/></svg>
      DOORS &amp;<br>WINDOWS
    </div>
    <p>Lorem ipsum dolor sit amet, consec-<br>teter adipiscing elit. Aenean commo-<br>do ligula eget dolor. Aenean massa.<br>Cum sociis natoque.</p>
    <div class="more"><svg width="12" height="12"><path d="M6 1v10M1 6h10" stroke="#fff" stroke-width="2"/></svg></div>
  </div>
</section>

<section class="abs band">
  <div class="abs band-photo" role="img" aria-label="Plumber working under a kitchen sink"></div>
  <p class="abs">Looking for someone to help get your listing ready to show? A complete Home Repair Solution? Did an inspection reveal repairs needed before closing? Brightlane Home Repairs can help!</p>
</section>

<section class="abs what">
  <h2 class="abs heading">WHAT WE DO</h2>
  <div class="abs rule-sub" style="top:112px">what we offer</div>
  <div class="abs card">
    <div class="abs card-photo" role="img" aria-label="Plumber fitting a chrome pipe"></div>
    <div class="abs card-text">
      <h3>BRIGHTLANE HOME REPAIRS AND</h3>
      <p>Lorem Ipsum is simply dummy text of the printing and typesetting industry. Lorem Ipsum has been the industry's standard dummy text ever since the 1500s, when an unknown printer took a galley of type and scrambled it to make a type specimen book. It has survived</p>
      <p>It was popularised in the 1960s with the release of Typeset sheets containing Lorem Ipsum passages, and more recently with desktop publishing software like Quill PageSetter including versions of Lorem Ipsum.</p>
    </div>
  </div>
  <form class="abs estimate">
    <h3>Request An Estimate Form</h3>
    <div class="field">Name</div>
    <div class="field">Email</div>
    <div class="field">Phone</div>
    <div class="field msg">Message</div>
    <div class="submit">SUBMIT</div>
  </form>
</section>

<section class="abs works">
  <h2 class="abs heading">COMPLETED WORKS</h2>
  <div class="abs rule-sub" style="top:92px">what we offer</div>
  <div class="abs filters"><span class="on">ALL</span><span>BATHROOM</span><span>KITCHEN</span><span>INSTALLATION</span></div>
  <div class="abs grid" role="img" aria-label="Gallery of ten completed plumbing and repair jobs">
    <div></div><div></div><div></div><div></div><div></div>
    <div></div><div></div><div></div><div></div><div></div>
  </div>
  <div class="abs view-all">View All</div>
</section>

<section class="abs testi">
  <h2 class="abs heading">OUR TESTIMONIALS</h2>
  <div class="abs rule-sub" style="top:110px">what we offer</div>
  <div class="abs quote-box red">Lorem ipsum dolor sit amet, consectetur adipisicing elit, sed do eiusmod tempor incididunt ut labore et dolore magna aliqua. Ut enim ad minim veniam, quis nostrud exercitation ullamco laboris nisi ut aliquip ex ea commodo consequat. Duis aute irure dolor.</div>
  <div class="abs tail" style="left:202px;top:362px;color:var(--red)"></div>
  <div class="abs quote-box dark">These guys solved my problem in a moment. Highly recommended!</div>
  <div class="abs tail" style="left:960px;top:362px;color:#222"></div>
  <div class="abs person" style="left:168px;top:395px">
    <div class="avatar" role="img" aria-label="Customer portrait"></div>
    <div><b>Jane Doe</b><small>Engineer of Media Production</small></div>
  </div>
  <div class="abs person" style="left:748px;top:377px;text-align:right">
    <div><b>Jane Doe</b><small>Engineer of Media Production</small></div>
    <div class="avatar" role="img" aria-label="Customer portrait"></div>
  </div>
</section>

<footer class="abs footer">
  <div class="abs brand" style="left:455px;top:50px">
    <div class="brand-mark"></div>
    <div class="brand-name">Brightlane Home Repairs<br><span style="font-size:13px">And Maintenance</span></div>
  </div>
  <div class="abs links">Home &bull; Solutions &bull; Services &bull; Company &bull; Contact</div>
  <div class="abs copy">Copyright 2016. Brightlane Home Repairs And Maintenance LLC. All rights reserved.</div>
  <div class="abs social"><span></span><span></span><span></span><span></span></div>
</footer>

</body>
</html>
```